Business Card Design

we are a brand new cable TV network devoted to self improvement and leading a better life called FLOURIVO TV.I have a logo. We have 3 executives that need cards.I want it to be a heavy stock card: professional but showing our creative nature

Industry/Entity Type

Business

Contact Information for Business Card

CLAUDIA SAENZ AMLIECEO350 San Juan DrPonte Vedra Beach FL 32082904-473-5953

```html
<!DOCTYPE html>
<html lang="en">
<head>
<meta charset="utf-8">
<title>FLOURIVO TV — Business Card</title>
<link href="https://fonts.googleapis.com/css2?family=Lato:wght@400;700;900&display=swap" rel="stylesheet">
<style>
  :root {
    --page-bg: #e9e7e4;
    --card-light: #ffffff;
    --card-dark: #231f20;
    --accent-red: #c8202a;
    --ink-dark: #231f20;
    --ink-light: #ffffff;
  }
  * { box-sizing: border-box; margin: 0; padding: 0; }
  html, body {
    width: 1200px;
    height: 978px;
    overflow: hidden;
    background: var(--page-bg);
    font-family: "Lato", Arial, sans-serif;
  }
  .canvas {
    position: relative;
    width: 1200px;
    height: 978px;
  }
  .card {
    position: absolute;
    width: 708px;
    height: 404px;
    border-radius: 10px;
    overflow: hidden;
    display: flex;
    box-shadow: 0 4px 10px rgba(0,0,0,0.25);
  }
  .card--top { left: 230px; top: 54px; }
  .card--bottom { left: 228px; top: 497px; }

  .card__brand-side {
    width: 350px;
    background: var(--card-light);
    border-right: 3px solid var(--accent-red);
    display: flex;
    align-items: center;
    justify-content: center;
  }
  .brand-name {
    font-weight: 900;
    font-size: 40px;
    letter-spacing: 0.5px;
    color: var(--ink-dark);
    display: flex;
    align-items: center;
    gap: 10px;
  }
  .brand-dot {
    width: 16px;
    height: 16px;
    border-radius: 50%;
    background: var(--accent-red);
  }

  .card__info-side {
    flex: 1;
    background: var(--card-dark);
    color: var(--ink-light);
    padding: 152px 0 0 21px;
  }
  .person-name,
  .person-title {
    font-weight: 700;
    font-size: 24px;
    line-height: 30px;
    text-transform: uppercase;
    letter-spacing: 0.2px;
  }
  .contact-list {
    list-style: none;
    margin-top: 22px;
    font-size: 20.5px;
    line-height: 24px;
  }
  .contact-item {
    display: flex;
    align-items: flex-start;
    gap: 8px;
  }
  .contact-icon {
    width: 18px;
    flex: 0 0 18px;
    margin-top: 4px;
    fill: var(--ink-light);
  }
</style>
</head>
<body>
<main class="canvas">

  <article class="card card--top">
    <div class="card__brand-side">
      <div class="brand-name"><span class="brand-dot"></span>FLOURIVO TV</div>
    </div>
    <div class="card__info-side">
      <p class="person-name">MIRELLA OKAFOR DUNST</p>
      <p class="person-title">CEO</p>
      <ul class="contact-list">
        <li class="contact-item">
          <svg class="contact-icon" viewBox="0 0 20 16" aria-hidden="true"><path d="M1 5c0-3 18-3 18 0v2h-4V5H5v2H1z"/><path d="M4 8h12l2 7H2z"/></svg>
          <span>541-618-2047</span>
        </li>
        <li class="contact-item">
          <svg class="contact-icon" viewBox="0 0 18 28" aria-hidden="true"><path d="M9 0a9 9 0 0 0-9 9c0 7 9 19 9 19s9-12 9-19a9 9 0 0 0-9-9zm0 13a4 4 0 1 1 0-8 4 4 0 0 1 0 8z"/></svg>
          <span>718 Harlow Creek Dr<br>Kestrel Haven Bay OR 97411</span>
        </li>
      </ul>
    </div>
  </article>

  <article class="card card--bottom">
    <div class="card__brand-side">
      <div class="brand-name"><span class="brand-dot"></span>FLOURIVO TV</div>
    </div>
    <div class="card__info-side">
      <p class="person-name">MIRELLA OKAFOR DUNST</p>
      <p class="person-title">CEO</p>
      <ul class="contact-list">
        <li class="contact-item">
          <svg class="contact-icon" viewBox="0 0 20 16" aria-hidden="true"><path d="M1 5c0-3 18-3 18 0v2h-4V5H5v2H1z"/><path d="M4 8h12l2 7H2z"/></svg>
          <span>541-618-2047</span>
        </li>
        <li class="contact-item">
          <svg class="contact-icon" viewBox="0 0 18 28" aria-hidden="true"><path d="M9 0a9 9 0 0 0-9 9c0 7 9 19 9 19s9-12 9-19a9 9 0 0 0-9-9zm0 13a4 4 0 1 1 0-8 4 4 0 0 1 0 8z"/></svg>
          <span>718 Harlow Creek Dr<br>Kestrel Haven Bay OR 97411</span>
        </li>
      </ul>
    </div>
  </article>

</main>
</body>
</html>
```